Buch-/eBook-Cover zum Thema Geldmanagement
Zielgruppe
ich benötige ein Buch-Cover (Vorder- und Rückseite) für das Buch Der Pfad der klaren Vermögensführung. Untertitel ist Innere Ruhe und Wohlstand vereint. Das genaue Format ist im Briefing hinterlegt
Aufgabenstellung
Schön wäre es, wenn das Cover hell gehalten wäre. Es soll hochwertig aussehen. Ich habe zwar eigenes Bild-Material angegeben, es können jedoch auch andere Vorschläge kommen.

```html
<!DOCTYPE html>
<html lang="de">
<head>
<meta charset="utf-8">
<title>Der Pfad der klaren Vermögensführung – Cover</title>
<link rel="stylesheet" href="https://fonts.googleapis.com/css2?family=Oswald:wght@600;700&family=Roboto:wght@400&display=swap">
<style>
  :root {
    --stage: #f3f4f6;
    --paper: #ffffff;
    --paper-shade: #eef0f5;
    --navy: #1a2a5e;
    --gold: #d59a32;
    --band: #0c1029;
    --rule: #8a8d96;
    --ink-soft: #2d2f36;
    --band-text: #f2f2f2;
  }
  * { margin: 0; padding: 0; box-sizing: border-box; }
  html, body {
    width: 930px; height: 1200px; overflow: hidden;
    background: var(--stage);
  }
  .canvas {
    position: relative; width: 930px; height: 1200px;
    display: flex; align-items: center; justify-content: center;
  }
  .cover {
    position: relative; width: 780px; height: 1140px;
    background: linear-gradient(180deg, var(--paper) 0%, var(--paper) 50%, var(--paper-shade) 100%);
    overflow: hidden;
    box-shadow: 0 6px 24px rgba(0,0,0,0.12);
  }
  .title-block {
    position: absolute; top: 70px; left: 0; right: 0;
    text-align: center;
    font-family: "Oswald", sans-serif; font-weight: 700;
    text-transform: uppercase;
  }
  .title-line { display: block; letter-spacing: 1px; }
  .title-line--lead { color: var(--navy); font-size: 80px; line-height: 1.08; }
  .title-line--accent { color: var(--gold); font-size: 132px; line-height: 1.12; }
  .title-line--close { color: var(--navy); font-size: 100px; line-height: 1.18; letter-spacing: 3px; }
  .subtitle {
    position: absolute; top: 640px; left: 120px; right: 120px;
    border-top: 2px solid var(--rule); border-bottom: 2px solid var(--rule);
    padding: 10px 0 12px;
    text-align: center;
    font-family: "Roboto", sans-serif; font-size: 27px;
    color: var(--ink-soft); text-transform: uppercase; letter-spacing: 0.5px;
  }
  .scene-photo {
    position: absolute; left: 0; right: 0; top: 720px; height: 250px;
    background: radial-gradient(ellipse at 50% 75%, #ffffff 0%, #e9ebf2 45%, #dadde8 100%);
  }
  .gold-rule {
    position: absolute; left: 0; right: 0; top: 970px; height: 8px;
    background: var(--gold);
  }
  .author-band {
    position: absolute; left: 0; right: 0; top: 978px; bottom: 0;
    background: var(--band);
    display: flex; align-items: center; justify-content: center;
  }
  .author-name {
    font-family: "Roboto", sans-serif; font-size: 32px;
    letter-spacing: 4px; color: var(--band-text); text-transform: uppercase;
  }
</style>
</head>
<body>
  <div class="canvas">
    <article class="cover">
      <h1 class="title-block">
        <span class="title-line title-line--lead">Der Pfad der</span>
        <span class="title-line title-line--accent">Klaren</span>
        <span class="title-line title-line--accent">Vermögens</span>
        <span class="title-line title-line--close">Führung</span>
      </h1>
      <p class="subtitle">Innere Ruhe und Wohlstand vereint</p>
      <div class="scene-photo" role="img" aria-label="Foto: gestapelte weiße Zen-Steine auf geharktem weißem Sand, darüber als Schmetterlinge gefaltete Geldscheine"></div>
      <div class="gold-rule"></div>
      <footer class="author-band">
        <span class="author-name">Author Name</span>
      </footer>
    </article>
  </div>
</body>
</html>
```